Ecommerce Software Provider Needs A Fresh Look For Website

We are looking for a fresh, new look for our existing ecommerce software service. We provide an ecommerce software targeted at small business owners called "QuickelShop" and our existing website can be seen at http://www.quickelshop-example.com.

QuickelShop helps small business owners build their online store instantly without any coding. We focus on not just building "online stores" but PROFITABLE online stores. As such, we focus on tools and features that help our clients create online stores that convert.

The "feel" we want to portray to our clients are as below:

- Powerful
- Easy to use
- Can start quickly
- Successful
- Profitable

We are open to pretty much any color scheme or feel. The only thing we absolutely want to retain is our company logo which uses a shade of green and black.

So, this is pretty much a "free reign" kind of project. Let your imagination and design juices run wild! :-)

Industry/Entity Type

Small Business

```html
<!DOCTYPE html>
<html lang="en">
<head>
<meta charset="utf-8">
<title>QuickelShop – Build once, sell instantly in 3 places</title>
<link href="https://fonts.googleapis.com/css2?family=Open+Sans:wght@300;400;600;700&family=Oswald:wght@300;400&family=Cormorant+Garamond:wght@400&display=swap" rel="stylesheet">
<style>
:root{
  --green:#a9c56b;
  --green-dark:#7aa332;
  --title-green:#4f9d2a;
  --ink:#2b2b2b;
  --body:#555;
  --muted:#777;
  --cream:#fdf9e3;
  --bar-grey:#c9c7a4;
  --bar-salmon:#f5b3a1;
  --bar-teal:#8dcfbd;
  --footer:#303e4d;
  --footer-line:#46566a;
  --footer-text:#c8d0d8;
  --white:#fff;
  --ic-pink:#f7c8b8;
  --ic-teal:#9ad4c5;
  --ic-tan:#e2d3b6;
  --ic-yellow:#f5d07a;
  --ic-green:#b6cf79;
}
*{margin:0;padding:0;box-sizing:border-box}
html,body{width:1200px;height:2214px;overflow:hidden}
body{font-family:"Open Sans",Arial,sans-serif;color:var(--body);background:var(--white);position:relative}
section,header,footer{position:absolute;left:0;width:1200px}
.abs{position:absolute}

/* header */
.site-header{top:0;height:71px;background:var(--white);border-bottom:1px solid #e6e6e6}
.brand{left:58px;top:18px;display:flex;align-items:center;gap:8px;font-weight:700;font-size:25px;color:var(--ink)}
.brand-dot{width:20px;height:20px;border-radius:50%;background:var(--green-dark)}
.util-links{right:58px;top:8px;display:flex;align-items:center;gap:14px;font-size:12px;color:var(--muted)}
.signup{background:var(--green-dark);color:var(--white);font-weight:700;padding:2px 9px;border-radius:2px;font-size:11px}
.main-nav{right:58px;top:44px;display:flex;gap:28px;font-size:13px;font-weight:600;color:#8a8a8a;letter-spacing:.2px}
.main-nav .active{color:var(--green-dark)}

/* hero */
.hero{top:71px;height:427px;background:var(--green);overflow:hidden}
.hero-kicker{left:84px;top:26px;font-family:"Cormorant Garamond",Georgia,serif;font-size:40px;color:var(--white);line-height:1}
.hero-title{left:82px;top:66px;font-family:"Oswald",Arial,sans-serif;font-weight:300;font-size:48px;color:var(--white);letter-spacing:.5px;line-height:1}
.hero-screens{left:262px;top:140px;width:405px;height:287px;background:linear-gradient(160deg,#f1f1f1,#d7dde6 55%,#c2ccd8);border-radius:3px}
.hero-cart{left:560px;top:20px;width:620px;height:400px;border-radius:30px;background:linear-gradient(135deg,rgba(255,255,255,.12),rgba(255,255,255,.04))}

/* three places */
.places{top:498px;height:266px;background:var(--cream)}
.bar{top:62px;height:28px}
.bar-first{border-radius:14px 0 0 14px}
.bar-last{border-radius:0 14px 14px 0}
.node{top:53px;width:46px;height:46px;border-radius:50%;display:flex;align-items:center;justify-content:center}
.place{top:125px;width:280px;text-align:center}
.place h3{font-weight:300;font-size:21px;margin-bottom:10px;white-space:nowrap}
.place p{font-size:13.5px;line-height:1.5;color:var(--body)}
.place .more{display:block;margin-top:14px;font-size:13px;color:var(--muted)}

/* reasons */
.reasons{top:764px;height:686px;background:var(--white)}
.reasons h2{position:absolute;left:0;width:1200px;top:48px;text-align:center;font-size:21px;font-weight:700;color:var(--title-green);letter-spacing:.3px}
.reason{width:400px;display:flex;gap:20px;align-items:flex-start}
.reason-icon{flex:0 0 58px;height:58px;border-radius:50%;display:flex;align-items:center;justify-content:center}
.reason p{font-size:13.3px;line-height:1.55;color:var(--ink)}

/* features */
.features{top:1450px;height:272px;background:var(--green)}
.feature{top:48px;width:440px;color:var(--white)}
.feature h3{font-size:21px;font-weight:600;line-height:1.3;color:#f6f9d8;margin-bottom:12px}
.feature p{font-size:13.3px;line-height:1.55}
.feature .more{display:block;margin-top:12px;font-size:13px}

/* clients */
.clients{top:1722px;height:127px;background:var(--white);display:flex;align-items:center;justify-content:center;gap:58px}
.client{font-size:25px;font-weight:700;color:#b9b9b9;display:flex;align-items:center;gap:8px}
.client-mark{width:34px;height:34px;border-radius:50%;background:#d3d3d3}

/* footer */
.site-footer{top:1849px;height:365px;background:var(--footer);color:var(--footer-text)}
.f-col h4{font-size:17px;font-weight:400;color:var(--white);margin-bottom:16px}
.f-col ul{list-style:none;font-size:12px;line-height:2.45}
.f-col .strong{font-weight:700;color:var(--white)}
.f-rule{left:148px;top:282px;width:904px;height:1px;background:var(--footer-line)}
.legal{left:148px;top:292px;font-size:11.5px;line-height:1.65}
.badge{left:800px;top:298px;width:96px;height:34px;background:#e9e9e9;border-radius:2px}
.socials{left:905px;top:300px;display:flex;gap:8px}
.socials span{width:29px;height:29px;border-radius:50%;background:#e9eef2;display:block}
</style>
</head>
<body>

<header class="site-header">
  <div class="abs brand"><span>QuickelShop</span><span class="brand-dot"></span></div>
  <div class="abs util-links"><span>Contact Us</span><span>Merchant Login</span><span class="signup">SIGN UP</span></div>
  <nav class="abs main-nav">
    <span class="active">CART FEATURES</span><span>PRICING</span><span>CREDIT CARDS</span><span>HAPPY CLIENTS EVERYWHERE!</span><span>ECOMMERCE TEMPLATES</span><span>ECOMMERCE BLOG</span>
  </nav>
</header>

<section class="hero">
  <div class="abs hero-cart" role="img" aria-label="Large faint shopping cart illustration"></div>
  <div class="abs hero-kicker">Build once,</div>
  <div class="abs hero-title">SELL INSTANTLY IN 3 PLACES...</div>
  <div class="abs hero-screens" role="img" aria-label="Collage of online store template screenshots"></div>
</section>

<section class="places">
  <div class="abs bar bar-first" style="left:277px;width:285px;background:var(--bar-grey)"></div>
  <div class="abs bar" style="left:562px;width:190px;background:var(--bar-salmon)"></div>
  <div class="abs bar bar-last" style="left:752px;width:244px;background:var(--bar-teal)"></div>
  <div class="abs node" style="left:283px;background:var(--bar-grey)">
    <svg width="24" height="20" viewBox="0 0 24 20"><rect x="2" y="2" width="20" height="14" rx="1" fill="none" stroke="#fff" stroke-width="2"/><rect x="8" y="17" width="8" height="2" fill="#fff"/></svg>
  </div>
  <div class="abs node" style="left:539px;background:var(--bar-salmon)">
    <svg width="24" height="18" viewBox="0 0 24 18"><rect x="1" y="1" width="22" height="16" rx="2" fill="none" stroke="#fff" stroke-width="2"/><rect x="1" y="5" width="22" height="3" fill="#fff"/></svg>
  </div>
  <div class="abs node" style="left:790px;background:var(--bar-teal)">
    <svg width="22" height="22" viewBox="0 0 22 22"><path d="M3 9h4v11H3zM9 9l3-7c2 0 3 1 3 3l-1 4h5c1 0 2 1 2 2l-2 8c0 1-1 1-2 1H9z" fill="#fff"/></svg>
  </div>
  <div class="abs place" style="left:159px"><h3 style="color:#b5b393">Beautiful Templates</h3><p>You need to attract attention within second or you've just lost your potential customer.</p><span class="more">See how →</span></div>
  <div class="abs place" style="left:469px"><h3 style="color:#f0a08c">Accept Payments Easily</h3><p>How should you let your customers pay you? credit card, PayWallet or Searchly</p><span class="more">Learn more →</span></div>
  <div class="abs place" style="left:768px"><h3 style="color:#6fc2ac">Sell on Friendbook</h3><p>Whether you like it or not, Friendbook is here to stay.</p><span class="more">Find out how →</span></div>
</section>

<section class="reasons">
  <h2>TOP 10 REASONS WHY PEOPLE CHOOSE QUICKELSHOP</h2>

  <div class="abs reason" style="left:148px;top:120px">
    <div class="reason-icon" style="background:var(--ic-pink)"><svg width="22" height="22" viewBox="0 0 22 22"><path d="M11 2l9 9-9 9-9-9z" fill="#fff"/></svg></div>
    <p>Complete all-in-one solution comes with your store builder, shopping cart, payment integration, ecommerce hosting, internet marketing tools and MUCH more...</p>
  </div>
  <div class="abs reason" style="left:626px;top:120px">
    <div class="reason-icon" style="background:var(--ic-pink)"><svg width="24" height="18" viewBox="0 0 24 18"><rect x="1" y="1" width="22" height="16" rx="2" fill="none" stroke="#fff" stroke-width="2"/><path d="M2 2l10 8 10-8" fill="none" stroke="#fff" stroke-width="2"/></svg></div>
    <p>Accept credit cards online with or without your own merchant account. Need a merchant account? We can offer you very competitive pricing as well</p>
  </div>

  <div class="abs reason" style="left:148px;top:231px">
    <div class="reason-icon" style="background:var(--ic-teal)"><svg width="24" height="22" viewBox="0 0 24 22"><path d="M2 4l6-3 4 3 4-3 6 3-3 4v13H5V8z" fill="#fff"/></svg></div>
    <p>Everyone loves free traffic. Your store pages are search engine optimized so that you rank higher on Searchly, Findr &amp; Yodel to tap into free search engine traffic</p>
  </div>
  <div class="abs reason" style="left:626px;top:231px">
    <div class="reason-icon" style="background:var(--ic-teal)"><svg width="24" height="22" viewBox="0 0 24 22"><circle cx="8" cy="7" r="4" fill="#fff"/><circle cx="17" cy="8" r="3" fill="#fff"/><path d="M1 21c0-6 3-9 7-9s7 3 7 9zM15 21c0-4 1-7 3-8 3 0 5 3 5 8z" fill="#fff"/></svg></div>
    <p>Site protected by strongest SSL security &amp; proprietary order fraud prevention included FREE with every account to keep you and your customers safe</p>
  </div>

  <div class="abs reason" style="left:148px;top:342px">
    <div class="reason-icon" style="background:var(--ic-tan)"><svg width="24" height="24" viewBox="0 0 24 24"><path d="M12 4a8 8 0 0 1 8 8" fill="none" stroke="#fff" stroke-width="2"/><path d="M12 20a8 8 0 0 1-8-8" fill="none" stroke="#fff" stroke-width="2"/><path d="M17 11l3 3 3-3zM1 13l3-3 3 3z" fill="#fff"/></svg></div>
    <p>Everyone loves free traffic. Your store pages are search engine optimized so that you rank higher on Searchly, Findr &amp; Yodel to tap into free search engine traffic</p>
  </div>
  <div class="abs reason" style="left:626px;top:342px">
    <div class="reason-icon" style="background:var(--ic-tan)"><svg width="26" height="18" viewBox="0 0 26 18"><rect x="4" y="1" width="18" height="12" rx="1" fill="none" stroke="#fff" stroke-width="2"/><rect x="1" y="14" width="24" height="3" fill="#fff"/></svg></div>
    <p>With more than 60 beautiful ecommerce templates to choose from, building an attractive &amp; stylish store is simply easy</p>
  </div>

  <div class="abs reason" style="left:148px;top:456px">
    <div class="reason-icon" style="background:var(--ic-yellow)"><svg width="22" height="24" viewBox="0 0 22 24"><rect x="2" y="2" width="18" height="20" rx="2" fill="none" stroke="#fff" stroke-width="2"/><path d="M6 8h10M6 12h10M6 16h6" stroke="#fff" stroke-width="2"/></svg></div>
    <p>Sometimes you just want things to be a certain way. QuickelShop is flexible to meet your needs. Heck, it's so flexible that you can even change every single word and image in your store!</p>
  </div>
  <div class="abs reason" style="left:626px;top:456px">
    <div class="reason-icon" style="background:var(--ic-yellow)"><svg width="24" height="22" viewBox="0 0 24 22"><path d="M2 2h20v13H9l-5 5v-5H2z" fill="#fff"/></svg></div>
    <p>Super-responsive customer service from REAL people who will bend over backwards to help you out. You won't get any "standard answers" from us</p>
  </div>

  <div class="abs reason" style="left:148px;top:567px">
    <div class="reason-icon" style="background:var(--ic-green)"><svg width="24" height="22" viewBox="0 0 24 22"><path d="M2 3h20v12H10l-5 4v-4H2z" fill="#fff"/></svg></div>
    <p>Super-competitive pricing. Unlike some of our competitors, we do NOT believe in having any hidden fees nor taking a percentage of your sales</p>
  </div>
  <div class="abs reason" style="left:626px;top:567px">
    <div class="reason-icon" style="background:var(--ic-green)"><svg width="20" height="24" viewBox="0 0 20 24"><rect x="1" y="1" width="18" height="22" rx="2" fill="#fff"/><path d="M5 8h10M5 12h10M5 16h10" stroke="#b6cf79" stroke-width="2"/></svg></div>
    <p>Super-stable and lightning-fast ecommerce hosting with 99.9% uptime guarantee makes sure your store is available all the time. Never miss a sale because your store is down</p>
  </div>
</section>

<section class="features">
  <div class="abs feature" style="left:150px">
    <h3>Shopping Cart<br>Software That Is Super Easy To Use...</h3>
    <p>Building your ecommerce store? Don't worry. Our simple point-and-click system lets you set up online store in no time. What if you're an ecommerce expert? Then, you'll be pleased to know that QuickelShop suits you as well.</p>
    <span class="more">See how →</span>
  </div>
  <div class="abs feature" style="left:627px">
    <h3>At Last! A Shopping Cart Software<br>That Helps You Sell More...</h3>
    <p>QuickelShop is one of the few ecommerce solutions that actually helps you to sell more. With built-in tools like our "people who bought this also bought this" feature, your store will literally urge people to buy more from you.</p>
    <span class="more">See how →</span>
  </div>
</section>

<section class="clients" aria-label="Client names">
  <span class="client"><span class="client-mark"></span></span>
  <span class="client">Vexora</span>
  <span class="client">Belvani</span>
  <span class="client">Q-Clip</span>
  <span class="client">Morwen</span>
  <span class="client">Cobalt Co</span>
  <span class="client">Harrowden</span>
</section>

<footer class="site-footer">
  <div class="abs f-col" style="left:148px;top:40px">
    <h4>QuickelShop.com</h4>
    <ul><li>Cart Features</li><li>Plans &amp; Pricing</li><li class="strong">30-Day Free Trial</li><li>Sign Up Now!</li><li>Client Showcase</li></ul>
  </div>
  <div class="abs f-col" style="left:308px;top:40px">
    <h4>&nbsp;</h4>
    <ul><li>Ecommerce Templates</li><li>See What Our Clients Say</li><li>Software Updates</li><li>Affiliates</li><li>About Us</li></ul>
  </div>
  <div class="abs f-col" style="left:566px;top:40px">
    <h4>Services</h4>
    <ul><li>Accept Credit Cards</li><li>Payment Gateways</li><li>Logo Design</li><li>Ecommerce Web Design</li><li>FREE Live Chat Software</li><li>Shopping Portal</li></ul>
  </div>
  <div class="abs f-col" style="left:816px;top:40px">
    <h4>Contact Us</h4>
    <ul><li>USA: +1-555-014-4188</li><li>Australia: +61-3-5550-9790</li><li>International: +60-4-5550-0704</li><li>Chat With Us</li><li>Ecommerce Support / Email Us</li><li>Existing Merchants: Support Ticket System</li></ul>
  </div>
  <div class="abs f-rule"></div>
  <div class="abs legal">
    © Copyright 2001-2014 Northleaf Digital Sdn. Bhd. All rights reserved<br>
    QuickelShop is a registered trademark of Northleaf Digital Sdn. Bhd. View Privacy Policy<br>
    Ecommerce software, ecommerce solutions &amp; QuickelShop shopping cart software provider
  </div>
  <div class="abs badge" aria-label="Security badge"></div>
  <div class="abs socials" aria-label="Social links"><span></span><span></span><span></span><span></span></div>
</footer>

</body>
</html>
```